Calverton Midstream Summary ESG brochure report

We are looking to create a summary ESG report for and Oil and Gas Midstream producer - Calverton Midstream. This is a report on their environmental, social and governance (ESG) aspects as well as a summary of who they are. It's focused on Wyoming oil and gas midstream for pipeline transport of oil and gas. We are to emphasize their environmental aspects, social aspects with visuals, graphics, etc. Attached is a example ESG report that is larger than what we want, but gives the designer of what an ESG report is.
The attached Harlowe 2019 report is an "IDEA of what we are looking for - but on a smaller scale. This is a much larger report, but expands on the idea of what we are trying to do.
Client is:
https://www.calvertonmidstream.example/
The outline brochure documens is what we have written and given examples of graphics with our writing / bullets of what we have visioned through the brochure. We are looking for a document with these items and graphs in it.
We have attached a few excel sheets and creations to hopefully better visualize our ideas and timelines to assist the graphic designers.

```html
<!DOCTYPE html>
<html lang="en">
<head>
<meta charset="utf-8">
<title>Calverton Midstream — Core Values</title>
<link rel="stylesheet" href="https://fonts.googleapis.com/css2?family=Montserrat:wght@400;700&family=Raleway:wght@400&family=Roboto+Mono:wght@400&display=swap">
<style>
  :root {
    --steel: #5b879f;
    --rust: #8b4a1f;
    --ink: #2b2b2b;
    --paper: #ffffff;
  }
  * { margin: 0; padding: 0; box-sizing: border-box; }
  html, body { width: 848px; height: 1200px; overflow: hidden; background: var(--paper); }
  .page { position: relative; width: 848px; height: 1200px; background: var(--paper); }
  .values-wheel { position: absolute; left: 0; top: 0; }
  .wheel-title { font-family: "Montserrat", sans-serif; font-weight: 700; font-size: 22px; fill: var(--steel); }
  .node-label { font-family: "Montserrat", sans-serif; font-weight: 700; font-size: 7px; fill: var(--paper); }
  .value { position: absolute; width: 260px; }
  .value-title { font-family: "Raleway", sans-serif; font-size: 17px; letter-spacing: 0.5px; color: var(--rust); line-height: 24px; margin-bottom: 6px; }
  .value-text { font-family: "Roboto Mono", monospace; font-size: 12.4px; line-height: 17.4px; color: var(--ink); }
  .value-icon { position: absolute; width: 62px; height: 62px; }
  .footer-band { position: absolute; left: 0; bottom: 0; width: 848px; height: 24px; background: var(--steel); }
</style>
</head>
<body>
<div class="page">

<svg class="values-wheel" width="848" height="430" viewBox="0 0 848 430">
  <defs>
    <symbol id="icon-safety" viewBox="0 0 40 40">
      <path d="M6 30 V16 a2 2 0 0 1 4 0 V12 a2 2 0 0 1 4 0 V11 a2 2 0 0 1 4 0 V14 a2 2 0 0 1 4 0 V26 q0 6 -6 6 h-4 q-6 0 -6 -2z" fill="#fff"/>
      <path d="M23 19 q5 -3 10 0 q1 7 -5 9 q-6 -2 -5 -9z" fill="#fff"/>
      <path d="M22 20 l-2 -1 M34 20 l2 -1" stroke="#fff" stroke-width="1.4"/>
    </symbol>
    <symbol id="icon-customer" viewBox="0 0 40 40">
      <circle cx="20" cy="20" r="5" fill="none" stroke="#fff" stroke-width="2"/>
      <path d="M10 33 q10 -11 20 0" fill="none" stroke="#fff" stroke-width="2"/>
      <path d="M20 4 l1.5 3 3 .4 -2.2 2 .6 3 -2.9 -1.5 -2.9 1.5 .6 -3 -2.2 -2 3 -.4z" fill="#fff"/>
      <path d="M8 13 l1.2 2.4 2.5 .3 -1.8 1.7 .5 2.5 -2.4 -1.3 -2.4 1.3 .5 -2.5 -1.8 -1.7 2.5 -.3z" fill="#fff"/>
      <path d="M32 13 l1.2 2.4 2.5 .3 -1.8 1.7 .5 2.5 -2.4 -1.3 -2.4 1.3 .5 -2.5 -1.8 -1.7 2.5 -.3z" fill="#fff"/>
    </symbol>
    <symbol id="icon-employees" viewBox="0 0 40 40">
      <circle cx="12" cy="9" r="3" fill="#fff"/><circle cx="20" cy="8" r="3" fill="#fff"/><circle cx="28" cy="9" r="3" fill="#fff"/>
      <rect x="9" y="13" width="6" height="7" rx="2" fill="#fff"/><rect x="17" y="12" width="6" height="8" rx="2" fill="#fff"/><rect x="25" y="13" width="6" height="7" rx="2" fill="#fff"/>
      <rect x="6" y="23" width="4" height="11" fill="#fff"/>
      <path d="M11 25 h9 q3 0 3 2 h-7 M11 32 h12 l10 -6 q-2 -2 -4 -1 l-6 3" fill="none" stroke="#fff" stroke-width="2"/>
    </symbol>
    <symbol id="icon-neighbor" viewBox="0 0 40 40">
      <path d="M4 34 V14 L12 6 L20 14 V34z M20 34 V14 L28 6 L36 14 V34z" fill="#fff"/>
      <circle cx="12" cy="18" r="2.5" fill="var(--steel)"/><circle cx="28" cy="18" r="2.5" fill="var(--steel)"/>
      <path d="M8 34 q4 -10 8 0 M24 34 q4 -10 8 0" fill="var(--steel)"/>
    </symbol>
    <symbol id="icon-handshake" viewBox="0 0 40 40">
      <path d="M3 14 l7 -3 7 3 -6 6 q2 2 4 0 l5 -4 10 8 -4 4 -3 -3 -2 3 -3 -3 -2 2 -3 -3 -2 2z" fill="#fff"/>
      <path d="M37 14 l-7 -3 -6 2 3 3 6 5 4 -2z" fill="#fff"/>
    </symbol>
    <symbol id="icon-gears" viewBox="0 0 40 40">
      <circle cx="15" cy="25" r="7" fill="none" stroke="#fff" stroke-width="4"/>
      <circle cx="15" cy="25" r="10" fill="none" stroke="#fff" stroke-width="3.5" stroke-dasharray="3.2 3"/>
      <circle cx="29" cy="11" r="4.5" fill="none" stroke="#fff" stroke-width="3"/>
      <circle cx="29" cy="11" r="7" fill="none" stroke="#fff" stroke-width="3" stroke-dasharray="2.5 2.5"/>
    </symbol>
    <symbol id="icon-bulb" viewBox="0 0 40 40">
      <path d="M20 6 a10 10 0 0 1 6 18 v4 h-12 v-4 a10 10 0 0 1 6 -18z" fill="#fff"/>
      <rect x="15" y="30" width="10" height="2.5" fill="#fff"/><rect x="16" y="34" width="8" height="2.5" fill="#fff"/>
      <path d="M20 1 v3 M8 9 l2 2 M32 9 l-2 2 M4 18 h3 M33 18 h3" stroke="#fff" stroke-width="1.3"/>
    </symbol>
  </defs>

  <circle cx="424" cy="241" r="106" fill="none" stroke="#222" stroke-width="1.3" stroke-dasharray="3 3"/>
  <text class="wheel-title" x="424" y="249" text-anchor="middle">CORE VALUES</text>

  <g fill="var(--steel)">
    <circle cx="424" cy="94" r="44"/><circle cx="547" cy="162" r="44"/><circle cx="565" cy="274" r="44"/>
    <circle cx="486" cy="370" r="44"/><circle cx="361" cy="370" r="44"/><circle cx="282" cy="274" r="44"/>
    <circle cx="300" cy="162" r="44"/>
  </g>

  <use href="#icon-safety" x="408" y="64" width="32" height="32"/>
  <text class="node-label" x="424" y="112" text-anchor="middle">SAFETY FIRST</text>

  <use href="#icon-neighbor" x="531" y="132" width="32" height="32"/>
  <text class="node-label" x="547" y="181" text-anchor="middle">GOOD</text>
  <text class="node-label" x="547" y="190" text-anchor="middle">NEIGHBOR</text>

  <use href="#icon-handshake" x="549" y="246" width="32" height="32"/>
  <text class="node-label" x="565" y="290" text-anchor="middle">INTEGRITY</text>

  <use href="#icon-gears" x="470" y="338" width="30" height="30"/>
  <text class="node-label" x="486" y="383" text-anchor="middle">SUPPLIERS &amp; SERVICE</text>
  <text class="node-label" x="486" y="392" text-anchor="middle">PROVIDERS</text>

  <use href="#icon-bulb" x="347" y="335" width="28" height="28"/>
  <text class="node-label" x="361" y="383" text-anchor="middle">INNOVATION &amp;</text>
  <text class="node-label" x="361" y="392" text-anchor="middle">CONTINUOUS</text>
  <text class="node-label" x="361" y="401" text-anchor="middle">IMPROVEMENT</text>

  <use href="#icon-employees" x="266" y="242" width="32" height="32"/>
  <text class="node-label" x="282" y="292" text-anchor="middle">COMMITTMENT</text>
  <text class="node-label" x="282" y="301" text-anchor="middle">TO EMPLOYEES</text>

  <use href="#icon-customer" x="284" y="125" width="32" height="32"/>
  <text class="node-label" x="300" y="181" text-anchor="middle">CUSTOMER</text>
  <text class="node-label" x="300" y="190" text-anchor="middle">FOCUS</text>
</svg>

<!-- Left column -->
<svg class="value-icon" style="left:67px;top:553px" viewBox="0 0 62 62"><circle cx="31" cy="31" r="31" fill="var(--steel)"/><use href="#icon-safety" x="15" y="15" width="32" height="32"/></svg>
<div class="value" style="left:154px;top:541px">
  <h2 class="value-title">Safety First</h2>
  <p class="value-text">We owe our employees and community a safe and accountable place to work. It is who we are.</p>
</div>

<svg class="value-icon" style="left:67px;top:701px" viewBox="0 0 62 62"><circle cx="31" cy="31" r="31" fill="var(--steel)"/><use href="#icon-employees" x="15" y="15" width="32" height="32"/></svg>
<div class="value" style="left:154px;top:686px">
  <h2 class="value-title">Commitment to Employees</h2>
  <p class="value-text">Our people are our greatest asset, ESGs focus is to provide opportunity to grow, learn, and develop in an inclusive environment.</p>
</div>

<svg class="value-icon" style="left:67px;top:865px" viewBox="0 0 62 62"><circle cx="31" cy="31" r="31" fill="var(--steel)"/><use href="#icon-neighbor" x="15" y="15" width="32" height="32"/></svg>
<div class="value" style="left:154px;top:853px">
  <h2 class="value-title">Good Neighbor</h2>
  <p class="value-text">Environmental responsibility with the land we are entrusted in the communities we love</p>
</div>

<svg class="value-icon" style="left:67px;top:1008px" viewBox="0 0 62 62"><circle cx="31" cy="31" r="31" fill="var(--steel)"/><use href="#icon-bulb" x="16" y="15" width="30" height="30"/></svg>
<div class="value" style="left:154px;top:986px">
  <h2 class="value-title">Innovation &amp; Continuous Improvement</h2>
  <p class="value-text">Speaks to how ESG is to develop within this organization and must remain a focus of innovation</p>
</div>

<!-- Right column -->
<svg class="value-icon" style="left:469px;top:553px" viewBox="0 0 62 62"><circle cx="31" cy="31" r="31" fill="var(--steel)"/><use href="#icon-customer" x="15" y="15" width="32" height="32"/></svg>
<div class="value" style="left:556px;top:541px">
  <h2 class="value-title">Customer Focus</h2>
  <p class="value-text">ESG focus on customer is reliable, sustainable, and safe operation</p>
</div>

<svg class="value-icon" style="left:469px;top:701px" viewBox="0 0 62 62"><circle cx="31" cy="31" r="31" fill="var(--steel)"/><use href="#icon-gears" x="15" y="15" width="32" height="32"/></svg>
<div class="value" style="left:556px;top:682px">
  <h2 class="value-title">Suppliers &amp; Service Providers</h2>
  <p class="value-text">Who we select as business partners is a reflection of who we are, it also is a means of mitigate risk</p>
</div>

<svg class="value-icon" style="left:469px;top:865px" viewBox="0 0 62 62"><circle cx="31" cy="31" r="31" fill="var(--steel)"/><use href="#icon-handshake" x="15" y="15" width="32" height="32"/></svg>
<div class="value" style="left:556px;top:853px">
  <h2 class="value-title">Integrity</h2>
  <p class="value-text">We must show responsible operation with an on-going commitment to environmental, health, and safety, corporate social accountability, corporate governance, sustainability, and other public policy matters relevant to our industry.</p>
</div>

<div class="footer-band"></div>
</div>
</body>
</html>
```